we need a business card. We are an online company that provides work life balance services to our members. our website can be viewed at www.qorvenly.com.au
Our company logo is attached as well as a business card look that i like.

```html
<!DOCTYPE html>
<html lang="en">
<head>
<meta charset="utf-8">
<title>Qorvenly Business Card</title>
<link rel="stylesheet" href="https://fonts.googleapis.com/css2?family=Arimo:ital,wght@0,400;0,700;1,400&display=swap">
<style>
  :root {
    --page-bg: #e8efe4;
    --green-deep: #1f7a36;
    --green-mid: #2f9444;
    --green-light: #8cc63f;
    --leaf-shade: #1a5e2a;
    --paper: #ffffff;
    --ink: #1c1c1c;
    --wordmark: #e4ece4;
    --tagline: #cfe0cf;
  }
  * { box-sizing: border-box; margin: 0; padding: 0; }
  html, body { width: 1200px; height: 1000px; overflow: hidden; }
  body {
    background: var(--page-bg);
    font-family: "Arimo", Arial, sans-serif;
    display: flex;
    align-items: center;
    justify-content: center;
    gap: 60px;
  }
  .card {
    position: relative;
    width: 525px;
    height: 300px;
    border-radius: 4px;
    overflow: hidden;
    box-shadow: 0 10px 28px rgba(0, 0, 0, 0.18);
  }

  /* Contact side */
  .card--contact { background: var(--paper); }
  .card__tab {
    position: absolute;
    top: 0; left: 0;
    width: 170px;
    height: 62px;
    background: linear-gradient(135deg, var(--green-mid), var(--green-deep));
    border-bottom-right-radius: 18px;
  }
  .contact-list {
    position: absolute;
    top: 86px;
    left: 30px;
    list-style: none;
    font-weight: 700;
    font-size: 15px;
    line-height: 27px;
    color: var(--ink);
  }
  .contact-list__label { display: inline-block; width: 18px; }
  .contact-list__slash {
    display: inline-block;
    width: 2px; height: 12px;
    margin: 0 9px 0 2px;
    background: var(--green-light);
    transform: skewX(-18deg);
    vertical-align: -1px;
  }
  .contact-list__gap { display: inline-block; width: 26px; }
  .contact-brand {
    position: absolute;
    right: 34px;
    bottom: 34px;
    display: flex;
    align-items: center;
    gap: 10px;
    font-size: 22px;
    font-weight: 400;
    color: var(--green-deep);
  }
  .contact-brand__dot {
    width: 14px; height: 14px;
    border-radius: 50%;
    background: var(--green-light);
  }

  /* Brand side */
  .card--brand {
    background: radial-gradient(ellipse at 60% 45%, #2a8a3c 0%, var(--green-deep) 60%, #186a2c 100%);
  }
  .card__foliage {
    position: absolute;
    top: 0; left: 0;
    width: 250px;
    height: 230px;
    background: radial-gradient(ellipse at 35% 35%, var(--leaf-shade) 0%, rgba(26, 94, 42, 0.5) 50%, rgba(26, 94, 42, 0) 75%);
  }
  .brand-block {
    position: absolute;
    left: 248px;
    top: 104px;
    color: var(--wordmark);
  }
  .brand-block__name {
    font-size: 52px;
    font-weight: 400;
    letter-spacing: 1px;
    line-height: 1;
  }
  .brand-block__tagline {
    margin-top: 8px;
    font-style: italic;
    font-size: 13px;
    letter-spacing: 0.5px;
    color: var(--tagline);
    white-space: nowrap;
  }
  .brand-block__divider { margin: 0 8px; }
</style>
</head>
<body>
  <section class="card card--contact" aria-label="Business card contact side">
    <div class="card__tab"></div>
    <ul class="contact-list">
      <li><span class="contact-list__label">P</span><span class="contact-list__slash"></span>02 5550 1847<span class="contact-list__gap"></span><span class="contact-list__label">F</span><span class="contact-list__slash"></span>02 5550 1848</li>
      <li><span class="contact-list__label">E</span><span class="contact-list__slash"></span>info@qorvenly.com.au</li>
      <li><span class="contact-list__label">W</span><span class="contact-list__slash"></span>www.qorvenly.com.au</li>
      <li><span class="contact-list__label">A</span><span class="contact-list__slash"></span>First Floor, 48 Harbour Lane</li>
      <li>Kirribilli Bay, NSW 2061</li>
    </ul>
    <div class="contact-brand">
      <span class="contact-brand__dot"></span>
      <span class="contact-brand__name">qorvenly</span>
    </div>
  </section>

  <section class="card card--brand" aria-label="Business card brand side">
    <div class="card__foliage" role="img" aria-label="Dark green leafy branch illustration"></div>
    <div class="brand-block">
      <div class="brand-block__name">qorvenly</div>
      <div class="brand-block__tagline">steady days<span class="brand-block__divider">|</span>stronger teams</div>
    </div>
  </section>
</body>
</html>
```